Dr Colin Pemberly needs a logo for letter head and business cards

I need a logo design for my stationery (letter head & business card). I am a Respiratory and Sleep medicine doctor who treats adults.
I treat asthma, snoring and other breathing problems and the symbols could include something relating to this. examples: ZZZ or a bed etc for snoring/sleep, a symbol of lungs , or other option. The blue lung could include a small red circle in the left one to indicate lung cancer.

Ideally in blue or green colour with maybe a small amount of red to indicate illness in the lung or somehow related to sleep.

the second side of the business card could include the text below:

Your next appointment is:
On ________________at_______________AM/PM

Please call to reschedule if necessary.

Target Market(s)

Middle aged to elderly patients and other medical staff. Professional context.

Industry/Entity Type

Medical

Contact Information for Business Card

Dr Colin Pemberly
MBBS (hons),
FRACP (Sleep & Respiratory).
DTM&H, MHSM, GC-CU.
www.harwoodclinicians.example

Locations:
Kestrel Private Specialist Consulting Rooms,
Level1, 517 Durnford Road,
Oakmere VIC 3187
Ph: 9461 7053
Fax: 8315 6640

Logo Text

that this is a respectable and trustworthy medical specialist

Font styles to use
Sans Serif

Colors
34a6d7
0655a3
33b8a4
00a88f
85cae6
ec1f27

Requirements
Must have
• my name in the logo . I have included my current business card and need to replace the logo/wording in the top right corner "Kestrel Private specialist Consulting Rooms" for my own personalised logo.
Nice to have
• symbol relating to lungs /breathing and sleep
Should not have
• Should not have the location in the logo of the business card

```html
<!DOCTYPE html>
<html lang="en">
<head>
<meta charset="utf-8">
<title>Dr Colin Pemberly – Stationery</title>
<link href="https://fonts.googleapis.com/css2?family=Saira+Condensed:wght@500&family=Open+Sans:wght@300;400;600;700&display=swap" rel="stylesheet">
<style>
  :root {
    --bg: #f4f5f7;
    --paper: #ffffff;
    --teal: #16a68c;
    --blue: #0d55a3;
    --grey: #7a7a7a;
    --ink: #111111;
    --frame: #555555;
  }
  html, body { margin: 0; padding: 0; overflow: hidden; }
  body { width: 1200px; height: 1200px; background: var(--bg); position: relative; font-family: "Open Sans", sans-serif; color: var(--ink); }
  .abs { position: absolute; }
  .wordmark { font-family: "Saira Condensed", sans-serif; font-weight: 500; color: var(--teal); line-height: 1; white-space: nowrap; text-align: right; }
  .tagline { font-family: "Open Sans", sans-serif; font-weight: 300; color: var(--grey); white-space: nowrap; line-height: 1; text-align: right; }
  .mark { border-radius: 50%; background: var(--teal); }

  /* primary logo */
  .hero-mark { left: 240px; top: 76px; width: 150px; height: 150px; }
  .hero-name { right: 655px; top: 248px; font-size: 86px; }
  .hero-tag { right: 663px; top: 342px; font-size: 25px; }

  /* mono logo */
  .mono-mark { left: 1028px; top: 42px; width: 66px; height: 66px; background: var(--grey); }
  .mono-name { right: 45px; top: 118px; font-size: 38px; color: var(--grey); }
  .mono-tag { right: 47px; top: 161px; font-size: 11px; }

  /* letterhead */
  .letterhead { left: 610px; top: 274px; width: 557px; height: 865px; background: var(--paper); border: 1px solid var(--frame); box-sizing: border-box; }
  .lh-address { left: 20px; top: 36px; font-size: 6.5px; line-height: 10.4px; color: #444; }
  .lh-address strong { font-size: 8px; font-weight: 600; color: #333; }
  .lh-mark { left: 466px; top: 24px; width: 38px; height: 38px; }
  .lh-name { right: 20px; top: 66px; font-size: 19px; }
  .lh-tag { right: 20px; top: 90px; font-size: 5.5px; }
  .lh-rule { left: 20px; top: 106px; height: 3px; }
  .rule-blue { background: var(--blue); }
  .rule-teal { background: var(--teal); }
  .lh-url { left: 232px; top: 835px; font-size: 6px; color: #555; }

  /* business card front */
  .card { left: 33px; width: 531px; background: var(--paper); border: 1px solid var(--frame); box-sizing: border-box; }
  .card-front { top: 473px; height: 322px; }
  .cf-mark { left: 374px; top: 22px; width: 74px; height: 74px; }
  .cf-name { right: 24px; top: 102px; font-size: 35px; }
  .cf-tag { right: 27px; top: 140px; font-size: 10.5px; }
  .cf-contact { right: 23px; top: 170px; text-align: right; font-size: 14.2px; line-height: 17.6px; }
  .cf-person { left: 23px; top: 220px; font-size: 13px; line-height: 17.6px; font-weight: 300; }
  .cf-person h1 { margin: 0; font-size: 17.5px; font-weight: 600; line-height: 21px; }
  .cf-band { left: -1px; bottom: -1px; height: 11px; }

  /* business card back */
  .card-back { top: 815px; height: 324px; font-size: 15px; }
  .cb-title { left: 39px; top: 32px; font-weight: 700; font-size: 14.5px; margin: 0; }
  .cb-row { left: 39px; height: 20px; width: 460px; }
  .cb-row span { position: absolute; bottom: 0; line-height: 1; }
  .cb-line { position: absolute; bottom: 2px; border-bottom: 1px solid #222; }
  .cb-note { left: 0; width: 100%; top: 282px; text-align: center; font-size: 14.5px; }
</style>
</head>
<body>

  <!-- primary logo -->
  <div class="abs mark hero-mark"></div>
  <div class="abs wordmark hero-name">Dr Colin Pemberly</div>
  <div class="abs tagline hero-tag">SPECIALIST CONSULTING ROOM</div>

  <!-- single-colour logo -->
  <div class="abs mark mono-mark"></div>
  <div class="abs wordmark mono-name">Dr Colin Pemberly</div>
  <div class="abs tagline mono-tag">SPECIALIST CONSULTING ROOM</div>

  <!-- letterhead -->
  <section class="abs letterhead">
    <div class="abs lh-address">
      <strong>Kestrel Private</strong><br>
      Specialist Consulting Rooms<br>
      517 Durnford Road,<br>
      Oakmere Vic 3187<br>
      Tel: 9461 7053<br>
      Fax: 8315 6640
    </div>
    <div class="abs mark lh-mark"></div>
    <div class="abs wordmark lh-name">Dr Colin Pemberly</div>
    <div class="abs tagline lh-tag">SPECIALIST CONSULTING ROOM</div>
    <div class="abs lh-rule rule-blue" style="width:400px;"></div>
    <div class="abs lh-rule rule-teal" style="left:420px;width:117px;"></div>
    <div class="abs lh-url">www.kestrelprivate.example</div>
    <div class="abs rule-teal" style="left:232px;top:845px;width:49px;height:2px;"></div>
    <div class="abs rule-blue" style="left:281px;top:845px;width:49px;height:2px;"></div>
  </section>

  <!-- business card front -->
  <section class="abs card card-front">
    <div class="abs mark cf-mark"></div>
    <div class="abs wordmark cf-name">Dr Colin Pemberly</div>
    <div class="abs tagline cf-tag">SPECIALIST CONSULTING ROOM</div>
    <div class="abs cf-contact">
      Kestrel Private<br>
      Specialist Consulting Rooms<br>
      517 Durnford Road,<br>
      Oakmere Vic 3187<br>
      Tel: 9461 7053<br>
      Fax: 8315 6640<br>
      www.kestrelprivate.example
    </div>
    <div class="abs cf-person">
      <h1>Dr Colin Pemberly</h1>
      MBBS(hon)<br>
      FRACP (Sleep &amp; Respiratory)<br>
      DTM&amp;H
    </div>
    <div class="abs cf-band rule-blue" style="width:344px;"></div>
    <div class="abs cf-band rule-teal" style="left:343px;width:188px;"></div>
  </section>

  <!-- business card back -->
  <section class="abs card card-back">
    <h2 class="abs cb-title">Your Nex appointment is:</h2>
    <div class="abs cb-row" style="top:86px;"><span style="left:0">On</span><i class="cb-line" style="left:21px;width:224px"></i><span style="left:249px">at</span><i class="cb-line" style="left:267px;width:132px"></i><span style="left:403px">am/pm</span></div>
    <div class="abs cb-row" style="top:130px;"><span style="left:0">On</span><i class="cb-line" style="left:21px;width:224px"></i><span style="left:249px">at</span><i class="cb-line" style="left:267px;width:132px"></i><span style="left:403px">am/pm</span></div>
    <div class="abs cb-row" style="top:174px;"><span style="left:0">On</span><i class="cb-line" style="left:21px;width:224px"></i><span style="left:249px">at</span><i class="cb-line" style="left:267px;width:132px"></i><span style="left:403px">am/pm</span></div>
    <div class="abs cb-row" style="top:217px;"><span style="left:0">On</span><i class="cb-line" style="left:21px;width:224px"></i><span style="left:249px">at</span><i class="cb-line" style="left:267px;width:132px"></i><span style="left:403px">am/pm</span></div>
    <p class="abs cb-note" style="margin:0">Please call 9461 to reschedule or cancel appointment.</p>
  </section>

</body>
</html>
```